Business Card for my building company

I would like the card to make a statement, so as soon as you see the card you think "wow nice card' and then read the details on the card its self. Also i would like to be able to put in the detail for the MUST HAVES so please Crete a box that i can alter depending on who in my business needs the cards. Thank you

Target Market(s)

Any one looking to build a house/ townhouse or duplex

Industry/Entity Type

Home Builder

Contact Information for Business Card

I would like the card to have the logo on the card and the must haves

Font styles to use
Sans Serif

Requirements
Must have
• Name
• Phone Number
• Email Address
• Website
• Licence Number
• Abn

```html
<!DOCTYPE html>
<html lang="en">
<head>
<meta charset="UTF-8">
<title>Harbour Build Co – Business Card</title>
<link href="https://fonts.googleapis.com/css2?family=Source+Sans+3:wght@400;600;700&display=swap" rel="stylesheet">
<style>
  :root {
    --page-bg: #e9e6e2;
    --card-top: #2a3642;
    --card-bottom: #1f2a34;
    --accent: #f2e27a;
    --text-light: #ffffff;
    --brand: #e9c46a;
  }
  * { margin: 0; padding: 0; box-sizing: border-box; }
  html, body {
    width: 1200px; height: 900px; overflow: hidden;
    background: var(--page-bg);
    font-family: "Source Sans 3", sans-serif;
  }
  .canvas { position: relative; width: 1200px; height: 900px; }
  .card {
    position: absolute;
    width: 556px; height: 342px;
    background: linear-gradient(170deg, var(--card-top) 0%, var(--card-bottom) 100%);
    box-shadow: 0 10px 28px rgba(0,0,0,0.25);
  }
  .card--front { left: 238px; top: 62px; }
  .card--back { left: 458px; top: 518px; }

  .brand {
    position: absolute;
    display: flex; align-items: center; gap: 12px;
    color: var(--brand);
    font-weight: 700;
    line-height: 1.0;
  }
  .brand__mark {
    width: 22px; height: 22px; border-radius: 50%;
    background: var(--brand); flex: none;
  }
  .brand__name { font-size: 38px; }
  .card--front .brand { left: 38px; top: 110px; width: 230px; }
  .card--back .brand { left: 50%; top: 50%; transform: translate(-50%, -50%); width: 240px; }

  .details {
    position: absolute; right: 24px; top: 84px;
    text-align: right;
    color: var(--text-light);
    font-size: 15px;
  }
  .details__name {
    color: var(--accent); font-size: 19px; font-weight: 600;
    margin-bottom: 12px;
  }
  .details__row {
    display: flex; justify-content: flex-end; align-items: center; gap: 10px;
    height: 20px;
  }
  .details__row svg { width: 12px; height: 12px; fill: var(--accent); }
  .details__licence { margin-top: 16px; }
  .details__label { color: var(--accent); }
  .details__licence .details__row { gap: 4px; height: 23px; }
</style>
</head>
<body>
<main class="canvas">

  <section class="card card--front">
    <div class="brand">
      <span class="brand__mark"></span>
      <span class="brand__name">Harbour Build Co</span>
    </div>

    <div class="details">
      <p class="details__name">Daniel Harper</p>
      <div class="details__row">
        <span>044-987 654 321</span>
        <svg viewBox="0 0 24 24" aria-hidden="true"><path d="M6.6 10.8a15 15 0 0 0 6.6 6.6l2.2-2.2a1 1 0 0 1 1-.25 11.4 11.4 0 0 0 3.6.6 1 1 0 0 1 1 1V20a1 1 0 0 1-1 1A17 17 0 0 1 3 4a1 1 0 0 1 1-1h3.5a1 1 0 0 1 1 1c0 1.25.2 2.45.57 3.57a1 1 0 0 1-.25 1z"/></svg>
      </div>
      <div class="details__row">
        <span>hello@harbourbuild.com</span>
        <svg viewBox="0 0 24 24" aria-hidden="true"><path d="M2 5h20v14H2z M2 5l10 8 10-8" /></svg>
      </div>
      <div class="details__row">
        <span>www.harbourbuild.com</span>
        <svg viewBox="0 0 24 24" aria-hidden="true"><circle cx="12" cy="12" r="10"/></svg>
      </div>
      <div class="details__licence">
        <div class="details__row"><span class="details__label">Licence Number</span></div>
        <div class="details__row"><span class="details__label">Abn:</span><span>987 654 321</span></div>
      </div>
    </div>
  </section>

  <section class="card card--back">
    <div class="brand">
      <span class="brand__mark"></span>
      <span class="brand__name">Harbour Build Co</span>
    </div>
  </section>

</main>
</body>
</html>
```